Moonlit Cascades: Your guide to Erotic, Sensual Enemas

I need a Readora eBook/RPX cover. size 6" (152mm) x 9 (228mm) front, same size rear cover. This is the first in my Moonlit Cascades series.

Introduction
This book features two stories; one introduces and explains the use of enemas to achieve sexual benefits; the second describes a struggle to hide Rolland Pike’ klismaphilia. Moonlit Cascades™ describes myriad aspects of “liquid refreshment for the anus”™. Enema enjoyment happily emerges from shadows of misunderstanding to its’ rightful bedroom welcome. If you are willing to experiment, enemas can become an occasional or regular feature in your Moonlit Cascades™ (MCqv™).

Rolland’s goal is to talk about the subject of enemas with those already having intimate experiences, to consider the possibility of enema experimentation. Many have heard it promoted as a new erogenous zone for intimacy & satisfaction; the medical title for this behavior is “klismaphilia”.

Until recently, Rolland could NEVER have imagined writing these words for you. Sexual enema enjoyment was his secret hidden from EVERYONE, much as some hid their non-heterosexual preference. He has now decided to emerge from his shadows of fear to discuss a life featuring klismaphiliac activities. Decades of use have provided the experience, knowledge and confidence to talk with others and provide relationship suggestions. He is optimistic you will discover enjoyment possibilities and topics for discussion, without his demons. Sexual activity using enemas has an equal role, with that of other adult toys, for satisfying adult entertainment.
Note: Though written from a male perspective, the orgasmic enjoyment from enemas works equally well with all genders and sexual preferences; the effects can be universally appreciated.

Please include symbol references to all sexes on the cover: http://www.glyphtabula.net/sign-marks.php use: male, female, double-male, double-female, interlocked male/femaleThank you. Added Wednesday, March 29, 2017

Self-help, sexually active adults,

Health And Wellness

Serif

9bcb3b

Must have
• Sensual appearance, sexually suggestive featuring images of male and female clothed buttocks. Add "10% of Profits donated to charity.!" to cover.
• Back cover; "About the Author" page.
Nice to have
• Humorous, Images of attractive male and female (tightly clothed) buttocks.
Should not have
• anything rude, or in bad taste, No skin

```html
<!DOCTYPE html>
<html lang="en">
<head>
<meta charset="utf-8">
<title>Moonlit Cascades: Your guide to Erotic, Sensual Enemas</title>
<link rel="stylesheet" href="https://fonts.googleapis.com/css2?family=Montserrat:wght@200;300;400&display=swap">
<style>
  :root {
    --stage: #e4e4e4;
    --cover-black: #000000;
    --lime: #b7e02c;
    --title-lime: #eaffb0;
    --lime-deep: #6f8f12;
    --lime-glow: rgba(190, 240, 50, 0.8);
    --ink-white: #ffffff;
  }
  html, body {
    margin: 0;
    padding: 0;
    width: 1200px;
    height: 848px;
    overflow: hidden;
    background: var(--stage);
  }
  .canvas {
    position: relative;
    width: 1200px;
    height: 848px;
  }
  .cover {
    position: absolute;
    left: 395px;
    top: 85px;
    width: 415px;
    height: 620px;
    background: var(--cover-black);
    overflow: hidden;
    font-family: "Montserrat", "Helvetica Neue", Arial, sans-serif;
  }
  .cover-photo {
    position: absolute;
    inset: 0;
    background:
      radial-gradient(ellipse 62% 16% at 45% 12%, rgba(180, 230, 40, 0.6), transparent 72%),
      radial-gradient(ellipse 40% 10% at 70% 24%, rgba(160, 210, 30, 0.45), transparent 75%),
      radial-gradient(ellipse 26% 42% at 30% 52%, rgba(120, 150, 20, 0.45), transparent 75%),
      radial-gradient(ellipse 20% 40% at 62% 62%, rgba(100, 130, 15, 0.35), transparent 75%),
      radial-gradient(ellipse 12% 45% at 88% 30%, rgba(90, 120, 15, 0.35), transparent 75%),
      var(--cover-black);
  }
  .title {
    position: absolute;
    left: 0;
    right: 0;
    top: 176px;
    margin: 0;
    text-align: center;
    font-weight: 200;
    font-size: 50px;
    line-height: 46px;
    letter-spacing: -0.5px;
    text-transform: uppercase;
    color: var(--title-lime);
    text-shadow: 0 0 3px var(--lime-glow), 0 0 10px var(--lime-glow), 0 0 22px var(--lime-deep);
  }
  .title span { display: block; }
  .gender-signs {
    position: absolute;
    left: 115px;
    top: 294px;
    width: 185px;
    height: 56px;
  }
  .gender-signs path,
  .gender-signs circle {
    fill: none;
    stroke: var(--ink-white);
    stroke-width: 3;
    stroke-linecap: butt;
  }
  .subtitle {
    position: absolute;
    left: 0;
    right: 0;
    top: 357px;
    margin: 0;
    text-align: center;
    font-weight: 300;
    font-size: 17px;
    line-height: 20px;
    text-transform: uppercase;
    color: var(--lime);
    text-shadow: 0 0 5px rgba(160, 210, 30, 0.45);
  }
  .charity-note {
    position: absolute;
    left: 0;
    right: 0;
    top: 575px;
    margin: 0;
    text-align: center;
    font-weight: 400;
    font-size: 8px;
    letter-spacing: 0.2px;
    text-transform: uppercase;
    color: var(--ink-white);
  }
</style>
</head>
<body>
<div class="canvas">
  <section class="cover">
    <div class="cover-photo" role="img" aria-label="Dark photograph of a figure's clothed hips in lime-green light, wrapped in glowing green smoke"></div>
    <h1 class="title"><span>Moonlit</span><span>Cascades:</span></h1>
    <svg class="gender-signs" viewBox="0 0 185 56" role="img" aria-label="Female, male, double male and interlocked female and male signs">
      <circle cx="13" cy="19" r="9"/>
      <path d="M13 28 V44 M6 36 H20"/>
      <circle cx="38" cy="30" r="9"/>
      <path d="M44.5 23.5 L54 14 M46 14 H54 V22"/>
      <circle cx="80" cy="33" r="9"/>
      <path d="M86.5 26.5 L96 17 M88 17 H96 V25"/>
      <circle cx="96" cy="27" r="9"/>
      <path d="M102.5 20.5 L112 11 M104 11 H112 V19"/>
      <circle cx="137" cy="26" r="9"/>
      <path d="M137 35 V52 M130 44 H144"/>
      <circle cx="151" cy="22" r="9"/>
      <path d="M157.5 15.5 L167 6 M159 6 H167 V14"/>
    </svg>
    <p class="subtitle">Your guide to erotic,<br>sensual enemas</p>
    <p class="charity-note">10% of profits donated to charity.</p>
  </section>
</div>
</body>
</html>
```